Attention grabbing 6x9 postcard

We are looking to have an attention grabbing post card that be sent out to homeowners from our roofing company Olum Roofing. the concept is that on the front it will say something like (STOP THE KNOCKING!
Tired of roofers knocking on your door? Contact us because we value your time as much as you value the roof over your head."
Olum Roofing
OlumRoofing.com
877.612.OLUM
info@olumroofing.com

Please feel free to come up with something very creative. Once we pick the final design we will provide the copy.

```html
<!DOCTYPE html>
<html lang="en">
<head>
<meta charset="utf-8">
<title>Olum Roofing Postcard</title>
<link rel="stylesheet" href="https://fonts.googleapis.com/css2?family=Bebas+Neue&family=Source+Sans+3:wght@400;600&family=Arimo:wght@400;700&display=swap">
<style>
  :root {
    --brand-gold: #d8b22c;
    --ink: #1c1c1c;
    --paper: #ffffff;
    --backdrop: #e6e6e6;
    --roof-light: #8a8c90;
    --roof-dark: #3e4044;
  }
  * { margin: 0; padding: 0; box-sizing: border-box; }
  html, body { width: 1200px; height: 745px; overflow: hidden; }
  body { background: var(--backdrop); position: relative; font-family: "Arimo", Arial, sans-serif; }

  .postcard { position: absolute; overflow: hidden; }

  /* Front */
  .postcard--front { left: 95px; top: 128px; width: 489px; height: 328px; }
  .front-photo {
    position: absolute; inset: 0;
    background: linear-gradient(160deg, var(--roof-light) 0%, #6a6c70 45%, var(--roof-dark) 100%);
  }
  .front-brand {
    position: absolute; left: 0; right: 0; top: 62px; text-align: center;
    font-family: "Source Sans 3", sans-serif; font-weight: 600; font-size: 34px;
    color: var(--paper); letter-spacing: 0.5px;
  }
  .front-brand__mark {
    display: inline-block; width: 14px; height: 14px; background: var(--paper);
    margin-right: 10px; vertical-align: 4px;
  }
  .front-url {
    position: absolute; left: 0; right: 0; top: 143px; text-align: center;
    font-family: "Source Sans 3", sans-serif; font-size: 21px; color: var(--paper);
  }
  .front-banner {
    position: absolute; left: 55px; top: 178px; width: 376px; height: 76px;
    background: var(--brand-gold); display: flex; align-items: center; justify-content: center;
  }
  .front-headline {
    font-family: "Bebas Neue", sans-serif; font-weight: 400; font-size: 49px;
    color: var(--paper); letter-spacing: 0.3px; line-height: 1; padding-top: 4px;
  }
  .front-pitch {
    position: absolute; left: 20px; right: 20px; top: 268px; text-align: center;
    font-family: "Source Sans 3", sans-serif; font-size: 15px; line-height: 18.5px; color: var(--paper);
  }

  /* Back */
  .postcard--back { left: 627px; top: 324px; width: 493px; height: 324px; background: var(--paper); }
  .back-content { position: absolute; left: 40px; top: 25px; width: 200px; }
  .back-heading {
    font-family: "Bebas Neue", sans-serif; font-weight: 400; font-size: 31px;
    line-height: 37px; color: var(--brand-gold);
  }
  .back-body { margin-top: 14px; font-size: 10.4px; line-height: 12.5px; color: var(--ink); }
  .back-points { margin-top: 16px; list-style: none; }
  .back-points li {
    position: relative; padding-left: 16px; font-size: 8.6px; line-height: 10.6px;
    font-weight: 700; color: var(--ink);
  }
  .back-points li::before {
    content: "•"; position: absolute; left: 2px; top: 0; color: var(--brand-gold);
  }
  .back-points .point-lead { color: var(--brand-gold); }

  .back-photo {
    position: absolute; left: 254px; width: 86px; height: 86px; border-radius: 9px;
  }
  .back-photo--roof { top: 17px; background: linear-gradient(170deg, #a7b0bb, #5f646b); }
  .back-photo--gable { top: 115px; background: linear-gradient(150deg, #6a6f7c, #c9ccd0); }
  .back-photo--brick { top: 214px; background: linear-gradient(180deg, #6d717a 0%, #8c7c68 60%, #6b5e50 100%); }

  .back-panel {
    position: absolute; right: 0; top: 0; width: 135px; height: 100%; background: var(--brand-gold);
  }
  .back-panel__brand {
    position: absolute; left: 0; right: 0; top: 102px; text-align: center;
    font-family: "Source Sans 3", sans-serif; font-weight: 600; font-size: 20px;
    line-height: 22px; color: var(--paper);
  }
  .back-panel__mark {
    display: block; width: 12px; height: 12px; background: var(--paper); margin: 0 auto 8px;
  }
  .back-contact {
    position: absolute; left: 20px; top: 263px; font-size: 9px; line-height: 11px;
    font-weight: 700; color: var(--paper); font-style: normal;
  }
</style>
</head>
<body>

  <section class="postcard postcard--front">
    <div class="front-photo" role="img" aria-label="Photo of grey asphalt shingle roof with a vent pipe"></div>
    <div class="front-brand"><span class="front-brand__mark"></span>Olum Roofing</div>
    <div class="front-url">OlumRoofing.com</div>
    <div class="front-banner"><h1 class="front-headline">STOP THE KNOCKING!</h1></div>
    <p class="front-pitch">Tired of roofers knocking on your door? Contact us because we value your time as much as you value the roof over your head.</p>
  </section>

  <section class="postcard postcard--back">
    <div class="back-content">
      <h2 class="back-heading">LOREM IPSUM DOLOR<br>SIT AMET,</h2>
      <p class="back-body">consectetuer adipiscing elit, sed diam nonummy nibh euismod tincidunt ut laoreet dolore magna aliquam erat volutpat. Ut wisi enim ad minim veniam, quis nostrud exerci tation ullamcorper suscipit lobortis nisl ut aliquip ex ea commodo consequat. Duis autem vel eum iriure dolor in hendrerit i</p>
      <ul class="back-points">
        <li><span class="point-lead">cipit lobortis nisl</span> ut aliquip ex ea commodo consequat.</li>
        <li><span class="point-lead">Duis autem</span> vel eum iriure dolor in hendrerit in vulputate</li>
        <li><span class="point-lead">velit esse molestie</span> consequat, vel illum dolore eu feugiat nulla facilisis at v</li>
      </ul>
    </div>

    <div class="back-photo back-photo--roof" role="img" aria-label="Photo of a shingle roof seen from above"></div>
    <div class="back-photo back-photo--gable" role="img" aria-label="Photo of a roof gable over a white sided house"></div>
    <div class="back-photo back-photo--brick" role="img" aria-label="Photo of a roof edge above a brick wall with a window"></div>

    <aside class="back-panel">
      <div class="back-panel__brand"><span class="back-panel__mark"></span>Olum<br>Roofing</div>
      <address class="back-contact">
        Olum Roofing<br>
        OlumRoofing.com<br>
        877.612.OLUM<br>
        info@olumroofing.com
      </address>
    </aside>
  </section>

</body>
</html>
```